Business Card Design for Orthopaedic Surgeon

This is a double-sided glossy business card. I prefer baby blue, teal, and green as color schemes. I have my logo already (many colors that you can choose from). I have photos and examples of my old card (very bland but has the information in it). I also have one that my assistant tried to design, but the writing is too small and I don't love the formatting. But it is close!
I would like my logo to be on the business card but I'm uploading my logo in many different colors so you can choose which one looks best based on the color scheme. I also uploaded many sized headshots so you can choose the best resolution one.

Additional information:
Correct business address:
4382 SE 58th Lane, Suite 305
Tamarac, FL 33347

Everything else on both business cards are accurate.

I actually need 2 different business cards generated. One that includes my cell phone number-- Personal cell: 585-614-3908 in addition to Office phone: (954) 362-5804 and Office Fax: 954-362-5819. Again, one card would have my personal cell and one wouldn't

Overall I just think the baby blue card (uploaded) is missing something on the front--of course it is also missing my office phone/fax/personal cell. I do want my website on the front too. Email: info@rkellowsurg.com

You can use your discretion about what goes on the front vs. what goes on the back to eliminated clutter.

Oh and on the back, I would like to list "Conditions Treated" (not specialties include). The list is:
Carpal Tunnel
Trigger Finger
Ganglion Cysts
Hand Tumors
Han & Wrist Arthritis
Hand, Wrist & Elbow Tendonitis
Fractures of the Hand, Wrist, Elbow and Humerus
Nerve Injuries of the Hand, Wrist & Elbow
Microsurgery
Wrist Arthroscopy
Endoscopic Surgery

Target Market(s)

Primary care doctors, Lawyers, patients

Industry/Entity Type

Medical

Contact Information for Business Card

Please see above in project description

Colors

Requirements
Must have
• -Correct office info, Board Certified Orthopaedic Hand & Upper Extremity Surgeon
Nice to have
• Something that is classy and wow!

```html
<!DOCTYPE html>
<html lang="en">
<head>
<meta charset="utf-8">
<title>Renata Kellow, MD – Business Card</title>
<link rel="stylesheet" href="https://fonts.googleapis.com/css2?family=Arimo:ital,wght@0,400;0,700;1,400;1,700&family=Cinzel:wght@700&family=Roboto+Condensed:wght@400&display=swap">
<style>
  :root {
    --page-bg: #e6e6e6;
    --card-bg: #050505;
    --gold: #c2a66c;
    --gold-deep: #b4975c;
    --tan-text: #e2cf9f;
    --white: #ffffff;
    --ink: #111111;
  }
  * { box-sizing: border-box; margin: 0; padding: 0; }
  html, body { width: 1200px; height: 1200px; overflow: hidden; }
  body {
    background: var(--page-bg);
    position: relative;
    font-family: "Arimo", Arial, sans-serif;
  }
  .card {
    position: absolute;
    left: 262px;
    width: 686px;
    height: 390px;
    background: var(--card-bg);
    border-radius: 22px;
    overflow: hidden;
  }
  .card--front { top: 165px; }
  .card--back { top: 653px; }

  /* Front */
  .brand {
    position: absolute;
    left: 32px;
    top: 52px;
    display: flex;
    align-items: center;
    gap: 10px;
    font-family: "Cinzel", serif;
    font-weight: 700;
    font-size: 26px;
    color: var(--gold);
  }
  .brand__dot {
    width: 14px; height: 14px;
    border-radius: 50%;
    background: var(--gold);
  }
  .doctor-name {
    position: absolute;
    left: 35px;
    top: 148px;
    font-family: "Cinzel", serif;
    font-weight: 700;
    font-size: 27px;
    color: var(--gold);
    letter-spacing: 0.2px;
  }
  .doctor-title {
    position: absolute;
    left: 37px;
    top: 184px;
    font-family: "Roboto Condensed", sans-serif;
    font-size: 19px;
    color: var(--white);
  }
  .doctor-email {
    position: absolute;
    left: 37px;
    top: 211px;
    font-style: italic;
    font-size: 17px;
    color: var(--white);
  }
  .address {
    position: absolute;
    left: 35px;
    top: 249px;
    font-size: 17px;
    line-height: 24px;
    color: var(--white);
  }
  .contact-divider {
    position: absolute;
    left: 225px;
    top: 253px;
    width: 1px;
    height: 68px;
    background: var(--white);
  }
  .phones {
    position: absolute;
    left: 246px;
    top: 249px;
    list-style: none;
    font-size: 17px;
    line-height: 24px;
    color: var(--white);
  }
  .phones li { display: flex; align-items: center; gap: 8px; }
  .phones svg { width: 13px; height: 13px; flex: none; }
  .headshot {
    position: absolute;
    right: 0;
    top: 0;
    width: 220px;
    height: 390px;
    background: radial-gradient(ellipse at 55% 35%, #5a3a2a 0%, #2a1a14 40%, #0a0a0a 75%);
  }
  .front-band {
    position: absolute;
    left: 0; top: 0;
    width: 686px; height: 390px;
  }
  .website {
    position: absolute;
    width: 100%;
    text-align: center;
    font-weight: 700;
    font-style: italic;
    font-size: 16px;
    letter-spacing: 4px;
  }
  .website--front { top: 357px; left: -5px; color: var(--ink); }
  .website--back { top: 303px; left: 0; color: var(--gold-deep); font-size: 18px; }

  /* Back */
  .conditions__heading {
    position: absolute;
    width: 100%;
    top: 74px;
    text-align: center;
    font-weight: 700;
    font-style: italic;
    font-size: 31px;
    color: var(--gold);
  }
  .rule {
    position: absolute;
    left: 313px;
    width: 60px;
    height: 1px;
    background: var(--gold-deep);
    opacity: 0.7;
  }
  .rule--top { top: 124px; }
  .rule--bottom { top: 285px; }
  .conditions__list {
    position: absolute;
    width: 100%;
    top: 141px;
    text-align: center;
    font-size: 19.5px;
    line-height: 26px;
    color: var(--tan-text);
  }
  .sep { font-size: 12px; vertical-align: 2px; padding: 0 4px; }
</style>
</head>
<body>

<section class="card card--front">
  <div class="headshot" role="img" aria-label="Portrait photo of the surgeon"></div>

  <svg class="front-band" viewBox="0 0 686 390" aria-hidden="true">
    <path d="M0 390 L0 380 Q120 338 389 332 Q600 334 686 377 L686 390 Z" fill="var(--gold)"/>
  </svg>

  <div class="brand"><span class="brand__dot"></span>RK Hand</div>

  <h1 class="doctor-name">Renata Kellow, MD</h1>
  <p class="doctor-title">Board Certified Orthopaedic Hand &amp; Upper Extremity Surgeon</p>
  <p class="doctor-email">info@rkellowsurg.com</p>

  <address class="address" style="font-style:normal">
    4382 SE 58th Lane<br>
    Suite 305<br>
    Tamarac, FL 33347
  </address>

  <div class="contact-divider"></div>

  <ul class="phones">
    <li>
      <svg viewBox="0 0 12 12"><rect x="3" y="0.5" width="6" height="11" rx="1" fill="none" stroke="var(--gold)" stroke-width="1.2"/><rect x="5" y="9" width="2" height="1" fill="var(--gold)"/></svg>
      (585) 614-3908
    </li>
    <li>
      <svg viewBox="0 0 12 12"><path d="M2.5 0.8 L4.5 0.8 L5.3 3.4 L4 4.5 Q5.2 7.2 7.5 8.2 L8.6 6.9 L11.2 7.7 L11.2 9.7 Q11 11.4 9 11.2 Q1 10 0.8 2.6 Q0.8 0.9 2.5 0.8 Z" fill="var(--gold)"/></svg>
      (954) 362-5804
    </li>
    <li>
      <svg viewBox="0 0 12 12"><rect x="3" y="1" width="6" height="4" fill="var(--gold)"/><rect x="0.5" y="5" width="11" height="6" rx="1" fill="var(--gold)"/><rect x="2.5" y="7" width="7" height="1" fill="var(--card-bg)"/></svg>
      (954) 362-5819
    </li>
  </ul>

  <p class="website website--front">www.rkellowsurg.com</p>
</section>

<section class="card card--back">
  <h2 class="conditions__heading">Conditions Treated</h2>
  <div class="rule rule--top"></div>
  <p class="conditions__list">
    Carpal Tunnel<span class="sep">●</span>Trigger Finger<span class="sep">●</span>Ganglion Cysts<span class="sep">●</span>Hand Tumors<br>
    Han &amp; Wrist Arthritis<span class="sep">●</span>Hand, Wrist &amp; Elbow Tendonitis<br>
    Fractures of the Hand, Wrist, Elbow and Humerus<br>
    Nerve Injuries of the Hand, Wrist &amp; Elbow<span class="sep">●</span>Microsurgery<br>
    Wrist Arthroscopy<span class="sep">●</span>Endoscopic Surgery
  </p>
  <div class="rule rule--bottom"></div>
  <p class="website website--back">www.rkellowsurg.com</p>
</section>

</body>
</html>
```